Ancient Art and Artifact information website

Hello Designers,
We are starting up a new website who talk abut and discusses an ancient arts artifacts. We would covering a wide range of countries ranging from Egypt, Greece, India, Syria, Rome, etc. My website name Tarn Wisp
Designs that fits with ancient theme and some kind of uniqueness would be accepted.
Requirements:
1) A home page design
2) Sub page design
3) A suitable logo
Sections can be added are featured ancient arts/places with short description followed by a more button, latest news, and comment section.
Add contents if you found relevant for this category of website. Ability to share the information through social media is desired.
Must be a responsive design. I look forward to designs which are mind blowing.
Number of Pages Required
2 page

```html
<!DOCTYPE html>
<html lang="en">
<head>
<meta charset="utf-8">
<title>Tarn Wisp — Ancient Arts Artifacts</title>
<link rel="stylesheet" href="https://fonts.googleapis.com/css2?family=Raleway:wght@400;500;600;700&family=Open+Sans:wght@400;600;700&display=swap">
<style>
:root{
  --gold:#b8893e;
  --gold-light:#d2a55a;
  --brown-dark:#2a1a08;
  --brown-nav:#3a2510;
  --ink:#1c1c1c;
  --text:#333;
  --white:#fff;
  --cream:#f6f3ee;
  --footer:#0e0d0c;
}
*{margin:0;padding:0;box-sizing:border-box}
html,body{width:1200px;height:3435px;overflow:hidden}
body{position:relative;background:var(--white);font-family:"Open Sans",Arial,sans-serif;color:var(--text)}
.abs{position:absolute}
.section{position:absolute;left:0;width:1200px}

/* Header */
.site-header{top:0;height:115px;background:linear-gradient(#3f2a12,#2c1c0a)}
.brand{left:246px;top:28px;display:flex;align-items:center;gap:12px}
.brand-dot{width:18px;height:18px;border-radius:50%;background:var(--gold)}
.brand-name{font-family:"Raleway",sans-serif;font-weight:600;font-size:26px;color:var(--gold);letter-spacing:1px}
.main-nav{left:424px;top:50px;display:flex;gap:38px;font-family:"Raleway",sans-serif;font-size:13px;font-weight:500;color:var(--gold-light);letter-spacing:.5px}
.main-nav .active{color:var(--white)}

/* Hero */
.hero{top:115px;height:487px;background:linear-gradient(180deg,#4a3a2a 0%,#6d5640 45%,#3d2d1f 100%)}
.hero-dots{left:570px;top:572px;display:flex;gap:6px}
.hero-dots span{width:9px;height:9px;border-radius:50%;background:#cbb89a}
.hero-dots span.on{background:var(--white)}

/* Headings */
.kicker{font-family:"Raleway",sans-serif;font-weight:500;font-size:26px;letter-spacing:7px;text-align:center;width:1200px;left:0}
.title{font-family:"Raleway",sans-serif;font-weight:600;font-size:50px;letter-spacing:11px;text-align:center;width:1200px;left:0;color:var(--gold)}
.lead{left:250px;width:700px;text-align:center;font-size:13.5px;line-height:17px;letter-spacing:.4px}

/* Welcome */
.welcome{top:602px;height:422px;background:var(--white)}
.welcome .kicker{color:var(--ink)}

/* Artifacts */
.artifacts{top:1024px;height:549px;background:linear-gradient(180deg,#3a2c1e,#4a3726 50%,#2c2117)}
.artifacts .title{top:50px;font-size:36px;letter-spacing:3px;color:var(--gold-light)}
.art-item{color:var(--white)}
.art-item h3{font-family:"Raleway",sans-serif;font-weight:700;font-size:17px;letter-spacing:.8px}
.art-item p{font-size:10.5px;line-height:13px;color:#ddd;margin-top:4px}
.art-item.right{text-align:right}
.art-photo{border-radius:50%;border:4px solid var(--white);width:100px;height:100px}
.art-center{left:503px;top:300px;width:140px;height:80px;text-align:center}
.art-center .brand-name{display:block;margin-top:22px;font-size:24px}

/* Featured */
.featured{top:1573px;height:701px;background:var(--white)}
.featured .kicker{top:20px;font-size:20px;color:var(--ink)}
.featured .title{top:42px;font-weight:500;font-size:46px;letter-spacing:12px}
.tabs{top:103px;width:1200px;left:0;text-align:center;font-family:"Raleway",sans-serif;font-weight:700;font-size:11.5px;color:var(--ink)}
.tabs span{margin:0 18px}
.grid{left:240px;top:156px;display:grid;grid-template-columns:repeat(3,231px);grid-auto-rows:231px;gap:7px}
.grid div{width:231px;height:231px}

/* News */
.news{top:2274px;height:524px;background:linear-gradient(180deg,#3d2a12,#6a4a1f 50%,#3a2710)}
.news .kicker{top:40px;color:var(--white)}
.news .title{top:70px;font-weight:500;color:var(--gold-light)}
.news .lead{top:136px;color:var(--white)}
.card{width:231px;height:268px;background:var(--cream);top:199px}
.card-photo{height:138px}
.card h4{font-family:"Raleway",sans-serif;font-weight:700;font-size:12px;color:var(--gold);letter-spacing:.5px;margin:14px 10px 6px}
.card p{font-size:9.5px;line-height:12px;color:#444;margin:0 10px}

/* Testimonials */
.testimonials{top:2798px;height:305px;background:var(--white)}
.testimonials .kicker{top:24px;color:var(--ink)}
.testimonials .title{top:58px;font-weight:500}
.quote-photo{left:545px;top:116px;width:110px;height:110px;border-radius:50%;border:4px solid var(--gold)}
.testimonials .lead{top:237px;color:var(--ink)}

/* Contact */
.contact{top:3103px;height:332px;background:linear-gradient(180deg,#1d1a17,#0f0e0d)}
.contact .kicker{top:30px;color:var(--white)}
.contact .title{top:60px;font-weight:500;color:var(--gold-light)}
.field{background:var(--white);font-size:8px;font-weight:700;color:#555;letter-spacing:.5px;padding:8px 10px}
.submit{left:263px;top:254px;width:674px;height:32px;background:var(--gold);color:var(--white);text-align:center;line-height:32px;font-family:"Raleway",sans-serif;font-weight:700;font-size:12px;letter-spacing:3px}
.copyright{left:270px;top:308px;font-size:9px;color:#ccc;font-weight:600}
</style>
</head>
<body>

<header class="section site-header">
  <div class="abs brand"><span class="brand-dot"></span><span class="brand-name">TARN WISP</span></div>
  <nav class="abs main-nav">
    <span class="active">HOME</span><span>ABOUT US</span><span>BROWSE COUNTRY</span><span>BLOGS</span><span>NEWS</span><span>FAQ</span><span>CONTACT US</span>
  </nav>
</header>

<section class="section hero" role="img" aria-label="Photograph of ancient Roman forum ruins with columns and a domed church at dusk"></section>
<div class="abs hero-dots"><span></span><span class="on"></span><span></span><span></span><span></span></div>

<section class="section welcome">
  <div class="abs kicker" style="top:34px">WELCOME TO</div>
  <div class="abs title" style="top:62px">TARN WISP</div>
  <p class="abs lead" style="top:118px">Welcome to Lorem ipsum dolor sit amet, consectetur adipiscing elit. Fusce fringilla iaculis ante vel ornareat orci non elit elementum efficitur. Donec nibh lectus, bibendum acliberoeu, sagittislips faucibus veleen volutpat euismod odiovel mollis Donec tincidunt pretium urna in vulputatet facilisis, mi eget sodales tincidunt, neque quam blandit diamis eros vitae neque. Maecenas finibus mi magna, sit orper mauris tempud accam facilisis dignissim ipsum in congue.</p>
  <p class="abs lead" style="top:240px">Donec tincidunt pretium urna in vulputate. Ut facilisis, mi eget sodales tincidunt, neque quam blandit diam, a aliquet felis eros vitae nes finibus mi magna, sit amet ullamcorper mauris tempus an posuere a neque sed accumsan. Nam facilisis dignissim ipsum in congue.</p>
  <p class="abs lead" style="top:325px">Lorem ipsum dolor sit amet, consectetur adipiscing elit. Fusce fringilla iaculis ante vel ornare. Nunc orci non elit elementum efficitur. Donec nibh lectus, bibendum ac libero eu, sagittis faucibus velit. Aenean volutpalipsmut euismod oellipsumis eros vitaere a neque sed accumsan.</p>
</section>

<section class="section artifacts">
  <div class="abs title">AN ANCIENT ARTS ARTIFACTS</div>

  <div class="abs art-item right" style="right:753px;top:148px"><h3>EGYPT ANCIENT ARTS ARTIFACTS</h3><p>Vestibulum aclipsum diam sit amet<br>quamveh icula elementum.</p></div>
  <div class="abs art-photo" style="left:458px;top:137px;background:linear-gradient(#c9a46a,#8a6535)" role="img" aria-label="Egyptian sphinx and pyramid photo"></div>

  <div class="abs art-photo" style="left:626px;top:169px;background:linear-gradient(#d88a4a,#8a4a2a)" role="img" aria-label="Roman amphitheatre photo for Greece"></div>
  <div class="abs art-item" style="left:733px;top:175px"><h3>GREECE ANCIENT ARTS ARTIFACTS</h3><p>Vestibulum aclipsum diam sit amet<br>quamveh icula elementum.</p></div>

  <div class="abs art-item right" style="right:822px;top:317px"><h3>SYRIA ANCIENT ARTS ARTIFACTS</h3><p>Vestibulum aclipsum diam sit amet<br>quamveh icula elementum.</p></div>
  <div class="abs art-photo" style="left:390px;top:289px;background:linear-gradient(#d9c3a0,#9c7a52)" role="img" aria-label="Domed mosque photo"></div>

  <div class="abs art-photo" style="left:642px;top:323px;background:linear-gradient(#9cc0e0,#e8e2d8)" role="img" aria-label="White marble mausoleum photo"></div>
  <div class="abs art-item" style="left:753px;top:349px"><h3>INDIA &nbsp;ANCIENT ARTS ARTIFACTS</h3><p>Vestibulum aclipsum diam sit amet<br>quamveh icula elementum.</p></div>

  <div class="abs art-item right" style="right:705px;top:439px"><h3>ROME ANCIENT ARTS ARTIFACTS</h3><p>Vestibulum aclipsum diam sit amet<br>quamveh icula elementum.</p></div>
  <div class="abs art-photo" style="left:509px;top:401px;background:linear-gradient(#c8804a,#7a3a22)" role="img" aria-label="Roman ruins photo"></div>

  <div class="abs art-center"><span class="brand-name">TARN WISP</span></div>
</section>

<section class="section featured">
  <div class="abs kicker">ARTS PLACES</div>
  <div class="abs title">FEATURED ANCIENT</div>
  <div class="abs tabs"><span>EGYPT ANCIENT PLACES</span>|<span>GREECE ANCIENT PLACES</span>|<span>INDIA ANCIENT PLACES</span>|<span>SYRIA ANCIENT PLACES</span>|<span>ROME ANCIENT PLACES</span></div>
  <div class="abs grid">
    <div role="img" aria-label="Carved marble palace archway" style="background:linear-gradient(#e4ddd2,#a89a88)"></div>
    <div role="img" aria-label="Great pyramid under blue sky" style="background:linear-gradient(#7ea6d8 0%,#c9a26a 45%,#9a7040)"></div>
    <div role="img" aria-label="Sphinx statue against blue sky" style="background:linear-gradient(#3a78c4,#c7a27a)"></div>
    <div role="img" aria-label="Colosseum at sunset" style="background:linear-gradient(#f0a040,#b0502a 60%,#5a3020)"></div>
    <div role="img" aria-label="Baroque fountain with turquoise water" style="background:linear-gradient(#d8d0c0,#bfb39c 60%,#3fb0b0)"></div>
    <div role="img" aria-label="Roman columns and terracotta buildings" style="background:linear-gradient(#e08a40,#b0502a 60%,#6a4a2a)"></div>
  </div>
</section>

<section class="section news">
  <div class="abs kicker">ARTS PLACES</div>
  <div class="abs title">LATES NEWS</div>
  <p class="abs lead">Donec tincidunt pretium urnavulputatet facilisis, megetsodales tinciduntegue quamblandit diama aliquetfelis eros vitae nequaecenas finibus mmagna, sit amet ullamcorper mauris tempusenean posuere a neque sed accumsan. Nam facilisis dignissim ipsum in congue.</p>

  <article class="abs card" style="left:227px">
    <div class="card-photo" role="img" aria-label="Ancient Greek ruins photo" style="background:linear-gradient(#e09a50,#a06030)"></div>
    <h4>GREECE ANCIENT PLACES</h4>
    <p>Fusce mattis condimentum nutrum mauris quemec libero finibus ullamcorper felis mattis neque volutpat sem euismod nunc tempor ligula aget orci.</p>
  </article>
  <article class="abs card" style="left:483px">
    <div class="card-photo" role="img" aria-label="Colosseum photo" style="background:linear-gradient(#6fa0d8,#c0703a)"></div>
    <h4>ROME ANCIENT PLACES</h4>
    <p>Fusce mattis condimentum nutrum mauris quemec libero finibus ullamcorper felis mattis neque volutpat sem euismod nunc tempor ligula aget orci.</p>
  </article>
  <article class="abs card" style="left:740px">
    <div class="card-photo" role="img" aria-label="Sphinx and pyramids photo" style="background:linear-gradient(#8ab4e0,#c8a068)"></div>
    <h4>EGYPT ANCIENT PLACES</h4>
    <p>Fusce mattis condimentum nutrum mauris quemec libero finibus ullamcorper felis mattis neque volutpat sem euismod nunc tempor ligula aget orci.</p>
  </article>
</section>

<section class="section testimonials">
  <div class="abs kicker">ARTS PLACES</div>
  <div class="abs title">TESTIMONIALS</div>
  <div class="abs quote-photo" role="img" aria-label="Colosseum photo" style="background:linear-gradient(#6fa0d8,#c0703a)"></div>
  <p class="abs lead">Donec tincidunt pretium urnavulputatet facilisis, megetsodales tinciduntegue quamblandit diama aliquetfelis eros vitae nequaecenas finibus mmagna, sit amet ullamcorper mauris tempusenean posuere a neque sed accumsan. Nam facilisis dignissim ipsum in congue.</p>
</section>

<section class="section contact">
  <div class="abs kicker">ARTS PLACES</div>
  <div class="abs title">CONTACT US</div>
  <div class="abs field" style="left:263px;top:126px;width:332px;height:25px">NAME *</div>
  <div class="abs field" style="left:602px;top:126px;width:335px;height:25px">EMAIL *</div>
  <div class="abs field" style="left:263px;top:160px;width:674px;height:85px">MESSAGE</div>
  <div class="abs submit">SUBMIT YOUR MESSAGE</div>
  <div class="abs copyright">Copyright 2017 Tarn Wisp. All Rights Reserved.</div>
</section>

</body>
</html>
```